HYPNO Business Card

provide hypnotherapy and counselling for addictions, weight loss, anxiety, depression, smoking, alcohol etc
i would like the design to fit in with a feeling of peace and tranquility

Industry/Entity Type

Hypnotherapy

Contact Information for Business Card

Lena Castrell
Clinical Hypnotherapist and Counsellor
BA Social Work
Dip Clinical Hypnotherapy and Psychotherapy

Phone: 0438175203
Email: abluegatehypnotherapy@quillbox.net

```html
<!DOCTYPE html>
<html lang="en">
<head>
<meta charset="utf-8">
<title>Lena Castrell – Business Card</title>
<link href="https://fonts.googleapis.com/css2?family=Arimo:wght@400&display=swap" rel="stylesheet">
<style>
  :root {
    --backdrop: #e9ebe6;
    --card: #fbfbfa;
    --green: #5aaa2e;
    --lime: #b9d531;
    --yellow: #e4e33a;
    --ink: #5b6378;
    --ink-soft: #6c7386;
    --placeholder: #dfe1e5;
  }
  * { margin: 0; padding: 0; box-sizing: border-box; }
  html, body { width: 1200px; height: 818px; overflow: hidden; }
  body {
    background: var(--backdrop);
    font-family: "Arimo", Arial, sans-serif;
    display: flex; align-items: center; justify-content: center;
  }
  .business-card {
    position: relative;
    width: 900px; height: 514px;
    background: var(--card);
    box-shadow: 0 10px 30px rgba(0,0,0,.18);
    overflow: hidden;
  }
  .band { position: absolute; left: 0; width: 100%; height: 92px; }
  .band--top { top: 0; background: linear-gradient(to bottom, var(--green), var(--lime) 55%, var(--yellow)); }
  .band--bottom { bottom: 0; background: linear-gradient(to top, var(--green), var(--lime) 55%, var(--yellow)); }

  .badges { position: absolute; left: 48px; top: 118px; width: 200px; height: 280px; }
  .badge-membership { position: absolute; left: 20px; top: 0; }
  .badge-listing { position: absolute; left: 24px; top: 200px; }

  .identity { position: absolute; left: 300px; top: 126px; color: var(--ink); }
  .identity__name { font-size: 44px; font-weight: 400; letter-spacing: .5px; margin-bottom: 10px; }
  .identity__role, .identity__quals { font-size: 19px; color: var(--ink-soft); line-height: 1.35; }

  .contact { position: absolute; left: 350px; top: 300px; list-style: none; color: var(--ink); }
  .contact__item { display: flex; align-items: center; gap: 16px; font-size: 22px; margin-bottom: 16px; }
  .contact__icon { width: 22px; height: 22px; flex: none; }
</style>
</head>
<body>
  <article class="business-card">
    <div class="band band--top"></div>
    <div class="band band--bottom"></div>

    <div class="badges">
      <svg class="badge-membership" width="160" height="160" viewBox="0 0 160 160" role="img" aria-label="Professional association membership badge">
        <circle cx="80" cy="80" r="76" fill="var(--placeholder)"/>
      </svg>
      <svg class="badge-listing" width="150" height="70" viewBox="0 0 150 70" role="img" aria-label="Practitioner register listing badge">
        <rect x="0" y="6" width="150" height="58" rx="4" fill="var(--placeholder)"/>
      </svg>
    </div>

    <header class="identity">
      <h1 class="identity__name">Lena Castrell</h1>
      <p class="identity__role">Clinical Hypnotherapist and Counsellor</p>
      <p class="identity__quals">BA Social Work Dip Clinical Hypnotherapy and Psychotherapy</p>
    </header>

    <ul class="contact">
      <li class="contact__item">
        <svg class="contact__icon" viewBox="0 0 24 24" aria-hidden="true">
          <path d="M6.6 3.5c.6-.3 1.3-.1 1.6.5l1.6 3c.3.6.1 1.2-.4 1.6l-1.4 1c.9 2 2.4 3.6 4.4 4.6l1-1.4c.4-.5 1.1-.7 1.6-.4l3 1.6c.6.3.8 1 .5 1.6l-1 1.8c-.4.7-1.2 1.1-2 .9C9.9 17.3 6.7 14.1 5.7 8.5c-.2-.8.2-1.6.9-2z" fill="var(--ink-soft)"/>
        </svg>
        <span>0438175203</span>
      </li>
      <li class="contact__item">
        <svg class="contact__icon" viewBox="0 0 24 24" aria-hidden="true">
          <rect x="2" y="5" width="20" height="14" rx="1" fill="#7d8fb5"/>
          <path d="M2.5 5.5 12 13l9.5-7.5" fill="none" stroke="#fff" stroke-width="1.5"/>
        </svg>
        <span>abluegatehypnotherapy@quillbox.net</span>
      </li>
    </ul>
  </article>
</body>
</html>
```